Pet Dryer Package Box Design

The original design which is from our team member and failed is attached below. Also, the package size is attached in the files.
We need to design the package of the pet dryer for an innovative pet product company called "MOVADEN". We developed innovative pet products for pet owners. We want to see designs that send signals of innovation and superiority to customers to increase the price premium. The original package design is attached below. The original version is denied by Brendley because they don't think our package shows the product worth $300. We want designs that local Americans think are worth the premium.

Target Market(s)

Pet Market

Requirements
Must have
• Our product picture and logo

```html
<!DOCTYPE html>
<html lang="en">
<head>
<meta charset="utf-8">
<title>Pet Hair Dryer – Package Front Panel</title>
<link rel="stylesheet" href="https://fonts.googleapis.com/css2?family=Exo+2:ital,wght@0,700;0,800;0,900;1,800;1,900&display=swap">
<style>
  :root {
    --stage: #eeeff1;
    --gold-light: #f3dc8a;
    --gold: #d4ab45;
    --gold-deep: #a9802a;
    --blue-deep: #0d2f86;
    --blue: #1747a8;
    --blue-light: #2f6cc9;
    --navy-badge: #1b2a5e;
    --ink: #141414;
    --white: #f4f4f2;
    --red: #e0211d;
    --photo-grey: #e7e6e2;
  }
  * { box-sizing: border-box; margin: 0; padding: 0; }
  html, body { width: 1200px; height: 675px; overflow: hidden; background: var(--stage); }
  body { position: relative; font-family: "Exo 2", sans-serif; }

  .front-panel {
    position: absolute; left: 290px; top: 28px;
    width: 620px; height: 620px; overflow: hidden;
    background: linear-gradient(135deg, var(--gold-deep) 0%, var(--gold) 30%, var(--gold-light) 60%, var(--gold) 100%);
  }
  .panel-art { position: absolute; inset: 0; width: 620px; height: 620px; }

  .pet-photo {
    position: absolute; left: 10px; top: 150px; width: 430px; height: 470px;
    background: radial-gradient(ellipse at 45% 50%, rgba(70,120,200,.55), rgba(23,71,168,0) 70%);
  }

  .product-name {
    position: absolute; left: 24px; top: 52px;
    display: flex; align-items: center; gap: 10px;
  }
  .product-name .mark { width: 16px; height: 16px; background: var(--ink); }
  .product-name span {
    font-weight: 900; font-size: 34px; color: var(--ink); letter-spacing: 1px;
  }

  .maker-name {
    position: absolute; left: 494px; top: 28px;
    font-weight: 800; font-size: 20px; color: var(--red); letter-spacing: .5px;
  }

  .title-banner {
    position: absolute; left: 22px; top: 232px; width: 560px; height: 108px;
    transform: rotate(-6.5deg); transform-origin: left center;
    display: flex; align-items: center; justify-content: center;
  }
  .title-banner svg { position: absolute; inset: 0; width: 100%; height: 100%; }
  .title-text {
    position: relative; font-style: italic; font-weight: 900; font-size: 60px;
    letter-spacing: -1px; color: var(--white); white-space: nowrap;
  }
  .title-text .accent { color: var(--red); }

  .product-photo {
    position: absolute; left: 389px; top: 347px; width: 193px; height: 178px;
    border-radius: 22px;
    background: linear-gradient(160deg, #f7f6f3, var(--photo-grey) 60%, #cfcdc8);
  }

  .volume-badge {
    position: absolute; left: 37px; top: 480px; width: 106px; height: 150px;
    background: var(--navy-badge); border-radius: 12px;
    padding-top: 22px; text-align: center;
    font-weight: 900; font-size: 40px; color: var(--white);
  }
</style>
</head>
<body>
  <main class="front-panel">
    <svg class="panel-art" viewBox="0 0 620 620" aria-hidden="true">
      <defs>
        <linearGradient id="blueField" x1="0" y1="0" x2="0" y2="1">
          <stop offset="0" stop-color="var(--blue-deep)"/>
          <stop offset=".55" stop-color="var(--blue)"/>
          <stop offset="1" stop-color="var(--blue-light)"/>
        </linearGradient>
      </defs>
      <path class="blue-field" fill="url(#blueField)"
        d="M0 235 C60 160 170 95 300 72 C330 66 345 48 350 40 C420 10 520 5 620 20 L620 620 L0 620 Z"/>
      <path class="blue-arc" fill="none" stroke="var(--blue-deep)" stroke-width="4"
        d="M318 46 C400 10 520 10 620 28"/>
      <path class="floor-wave" fill="var(--blue-light)" opacity=".55"
        d="M0 585 C180 555 400 540 620 520 L620 620 L0 620 Z"/>
    </svg>

    <div class="pet-photo" role="img" aria-label="Faint photo of a fluffy dog tinted blue"></div>

    <div class="product-name"><i class="mark"></i><span>AIRO PRIME</span></div>
    <div class="maker-name">MOVADEN</div>

    <div class="title-banner">
      <svg viewBox="0 0 560 108" preserveAspectRatio="none" aria-hidden="true">
        <path d="M22 4 H552 Q560 4 556 14 L530 96 Q527 104 518 104 H8 Q0 104 3 96 L14 12 Q16 4 22 4 Z"
          fill="var(--ink)" stroke="var(--gold)" stroke-width="5"/>
      </svg>
      <h1 class="title-text">PET <span class="accent">HAIR</span> DRYER</h1>
    </div>

    <div class="product-photo" role="img" aria-label="Photo of the white pet drying box with a cat inside"></div>

    <div class="volume-badge">60 L</div>
  </main>
</body>
</html>
```